Beer Bottles and 6 Pack Case Design

Our Brewery's name is Quarry42 Brewing. We are looking for SEVEN bottle label designs. We are making this one project because we need all seven of the bottles labels to be different, but follow the same theme (as you will see in the attachments). The same goes for the six pack case design, same theme. As an added perk for the designers, we are willing to put "design by (you or your company)" on the bottle label designs and the six pack case. This will be seen by millions!!

The following are the names of our beers:
1) Plucked Wombat
2) KanTurnipo Jamma
3) Pearcastle Nectar
4) Runway Fringe IPA
5) Blue Cold Half-Aunt
6) Androids Called Otto
7) Copper Mule Limited

Our logo is also attached, please incorporate that into the designs (OR it can go on the neck of the bottle). If you have ANY questions, do not hesitate to ask!
Updates

Budgets for 2nd and 3rd place have been increased...

Project Deadline Extended
Reason: After posting this project I got very busy with other things and have not given this the attention I should have and have not responded to questions. Therefore I am going to extend the deadline by 7 days and answer all questions the best I can..

We have increased our first place budget to $500!!! 2nd and third place still get $100 each!!

Target Market(s)

The target market will be women and men, ages 24-34 with a slight focus towards the female demographic. Our target market annual income will be classified as middle to upper-middle class ($30,000- $60,000 annually).

Industry/Entity Type

It Company

Requirements
Nice to have
• Some sort of sketch of our "Characters" incorporated into the design.
Should not have
• -Many are submitting designs for the "androids called otto" label with pictures of t-rex dinosaurs. We would like just robots, no t-rex''s. Maybe a sketch of a few robots all with a "Hi My Name Is" sticker on them (like the stickers you get when you go to a big event. I have added an example of those stickers to the project attachments).
-We like the idea of a silly sketch of a donkey (possibly with a conductor hat and a whistle, but not a must) for the Copper Mule Limited label.
-We like the idea of a silly sketch of a shaven or partially shaven chinchilla for the Plucked Wombat label.
-We like the idea of a sketch of a women''s figure from behind with apples in place of her cheeks

Please take a look at the project attachment with the 9th Avenue beer bottle labels...we are leaning towards something along that sketch style design.

```html
<!DOCTYPE html>
<html lang="en">
<head>
<meta charset="utf-8">
<title>Quarry42 Brewing – Label Range</title>
<link rel="stylesheet" href="https://fonts.googleapis.com/css2?family=Oswald:wght@400;500&family=Roboto+Condensed:wght@400&display=swap">
<style>
  :root {
    --canvas: #cbc9b9;
    --band: #687a94;
    --label-paper: #d7d4c4;
    --label-edge: #b9b6a6;
    --title-grey: #7c8da2;
    --body-ink: #5a6677;
    --green: #1f6b33;
    --silver: #8e8f8f;
    --magenta: #8c1a5e;
    --lime: #8cc028;
    --navy: #1d3b6c;
    --red: #a2242b;
    --yellow: #f1b513;
  }
  * { box-sizing: border-box; margin: 0; padding: 0; }
  html, body { width: 1200px; height: 821px; overflow: hidden; background: var(--canvas); }
  .canvas { position: relative; width: 1200px; height: 821px; background: var(--canvas); }
  .label-band {
    position: absolute; left: 0; top: 262px; width: 1200px; height: 300px;
    background: var(--band);
    display: flex; justify-content: center; align-items: center; gap: 14px;
  }
  .label {
    width: 152px; height: 240px;
    background: var(--label-paper);
    border-top: 6px solid var(--accent);
    box-shadow: inset 0 0 0 1px var(--label-edge), 1px 2px 3px rgba(0,0,0,.35);
    display: flex; flex-direction: column; align-items: center;
    padding: 12px 8px 8px;
    font-family: "Oswald", sans-serif;
  }
  .label--green { --accent: var(--green); }
  .label--silver { --accent: var(--silver); }
  .label--magenta { --accent: var(--magenta); }
  .label--lime { --accent: var(--lime); }
  .label--navy { --accent: var(--navy); }
  .label--red { --accent: var(--red); }
  .label--yellow { --accent: var(--yellow); }
  .beer-name { text-align: center; text-transform: uppercase; font-weight: 500; line-height: 1.02; height: 72px; display: flex; flex-direction: column; justify-content: center; }
  .beer-name__top { display: block; color: var(--title-grey); font-size: var(--top-size, 28px); }
  .beer-name__bottom { display: block; color: var(--accent); font-size: var(--bottom-size, 27px); }
  .brewery-mark { display: flex; align-items: center; gap: 4px; margin-top: 10px; }
  .brewery-mark__dot { width: 12px; height: 12px; border-radius: 50%; background: var(--title-grey); }
  .brewery-mark__name { font-family: "Oswald", sans-serif; font-weight: 500; font-size: 12px; color: var(--title-grey); text-transform: uppercase; letter-spacing: .4px; }
  .beer-notes {
    margin-top: 12px; font-family: "Roboto Condensed", sans-serif;
    font-size: 5.4px; line-height: 1.35; color: var(--body-ink); text-align: left; width: 122px;
  }
  .label-footer {
    margin-top: auto; width: 122px; display: flex; justify-content: space-between; align-items: baseline;
    font-family: "Oswald", sans-serif; color: var(--title-grey); text-transform: uppercase;
  }
  .label-footer__volume, .label-footer__abv { font-size: 8px; }
  .label-footer__style { font-size: 11px; }
</style>
</head>
<body>
<main class="canvas">
  <section class="label-band">

    <article class="label label--green" style="--top-size:28px;--bottom-size:23px">
      <h2 class="beer-name"><span class="beer-name__top">Androids</span><span class="beer-name__bottom">Called Otto</span></h2>
      <div class="brewery-mark"><span class="brewery-mark__dot"></span><span class="brewery-mark__name">Quarry42 Brewing</span></div>
      <p class="beer-notes">Brewed slow in small batches from local malt and whole hops. Pours clear with a soft white head and a clean dry finish. Best served cold and shared with good friends on long evenings.</p>
      <div class="label-footer"><span class="label-footer__volume">33cl</span><span class="label-footer__style">Brown</span><span class="label-footer__abv">4,5%</span></div>
    </article>

    <article class="label label--silver" style="--top-size:22px;--bottom-size:30px">
      <h2 class="beer-name"><span class="beer-name__top">Copper Mule</span><span class="beer-name__bottom">Limited</span></h2>
      <div class="brewery-mark"><span class="brewery-mark__dot"></span><span class="brewery-mark__name">Quarry42 Brewing</span></div>
      <p class="beer-notes">Brewed slow in small batches from local malt and whole hops. Pours clear with a soft white head and a clean dry finish. Best served cold and shared with good friends on long evenings.</p>
      <div class="label-footer"><span class="label-footer__volume">33cl</span><span class="label-footer__style">Blonde</span><span class="label-footer__abv">4,5%</span></div>
    </article>

    <article class="label label--magenta" style="--top-size:28px;--bottom-size:24px">
      <h2 class="beer-name"><span class="beer-name__top">Runway</span><span class="beer-name__bottom">Fringe IPA</span></h2>
      <div class="brewery-mark"><span class="brewery-mark__dot"></span><span class="brewery-mark__name">Quarry42 Brewing</span></div>
      <p class="beer-notes">Brewed slow in small batches from local malt and whole hops. Pours clear with a soft white head and a clean dry finish. Best served cold and shared with good friends on long evenings.</p>
      <div class="label-footer"><span class="label-footer__volume">33cl</span><span class="label-footer__style">Dark</span><span class="label-footer__abv">4,5%</span></div>
    </article>

    <article class="label label--lime" style="--top-size:24px;--bottom-size:30px">
      <h2 class="beer-name"><span class="beer-name__top">Pearcastle</span><span class="beer-name__bottom">Nectar</span></h2>
      <div class="brewery-mark"><span class="brewery-mark__dot"></span><span class="brewery-mark__name">Quarry42 Brewing</span></div>
      <p class="beer-notes">Brewed slow in small batches from local malt and whole hops. Pours clear with a soft white head and a clean dry finish. Best served cold and shared with good friends on long evenings.</p>
      <div class="label-footer"><span class="label-footer__volume">33cl</span><span class="label-footer__style">Sweet</span><span class="label-footer__abv">4,5%</span></div>
    </article>

    <article class="label label--navy" style="--top-size:28px;--bottom-size:26px">
      <h2 class="beer-name"><span class="beer-name__top">Plucked</span><span class="beer-name__bottom">Wombat</span></h2>
      <div class="brewery-mark"><span class="brewery-mark__dot"></span><span class="brewery-mark__name">Quarry42 Brewing</span></div>
      <p class="beer-notes">Brewed slow in small batches from local malt and whole hops. Pours clear with a soft white head and a clean dry finish. Best served cold and shared with good friends on long evenings.</p>
      <div class="label-footer"><span class="label-footer__volume">33cl</span><span class="label-footer__style">Bitter</span><span class="label-footer__abv">4,5%</span></div>
    </article>

    <article class="label label--red" style="--top-size:28px;--bottom-size:25px">
      <h2 class="beer-name"><span class="beer-name__top">Blue Cold</span><span class="beer-name__bottom">Half-Aunt</span></h2>
      <div class="brewery-mark"><span class="brewery-mark__dot"></span><span class="brewery-mark__name">Quarry42 Brewing</span></div>
      <p class="beer-notes">Brewed slow in small batches from local malt and whole hops. Pours clear with a soft white head and a clean dry finish. Best served cold and shared with good friends on long evenings.</p>
      <div class="label-footer"><span class="label-footer__volume">33cl</span><span class="label-footer__style">Fruity</span><span class="label-footer__abv">4,5%</span></div>
    </article>

    <article class="label label--yellow" style="--top-size:23px;--bottom-size:30px">
      <h2 class="beer-name"><span class="beer-name__top">KanTurnipo</span><span class="beer-name__bottom">Jamma</span></h2>
      <div class="brewery-mark"><span class="brewery-mark__dot"></span><span class="brewery-mark__name">Quarry42 Brewing</span></div>
      <p class="beer-notes">Brewed slow in small batches from local malt and whole hops. Pours clear with a soft white head and a clean dry finish. Best served cold and shared with good friends on long evenings.</p>
      <div class="label-footer"><span class="label-footer__volume">33cl</span><span class="label-footer__style">Fruity</span><span class="label-footer__abv">4,5%</span></div>
    </article>

  </section>
</main>
</body>
</html>
```